Harborlyte Business Cards

I need a business card designed with the following information.

Company Name: Harborlyte Wealth Management
Name: BriAnne Dockery
Title: Executive Assistant
Cell: (555) 210-0173
Direct Line: (555) 310-0148
Email: brianne@harborwmx.com
Address: 20537 W. Marlowe PKWY Ste. B
Calderwick, QZ 00390

I have attached the logo.
I would like it in navy blue and silver.
Thanks.

```html
<!DOCTYPE html>
<html lang="en">
<head>
<meta charset="utf-8">
<title>Harborlyte Wealth Management – Business Card</title>
<link href="https://fonts.googleapis.com/css2?family=Open+Sans:wght@400;600;700&display=swap" rel="stylesheet">
<style>
  :root {
    --backdrop: #1b1c1e;
    --navy-deep: #0d2a49;
    --navy-mid: #1b4469;
    --navy-light: #2a5b82;
    --silver: #e4e7ea;
    --white: #ffffff;
  }
  * { margin: 0; padding: 0; box-sizing: border-box; }
  html, body {
    width: 1200px;
    height: 900px;
    overflow: hidden;
    background: var(--backdrop);
    font-family: "Open Sans", Arial, sans-serif;
  }
  .canvas {
    width: 1200px;
    height: 900px;
    display: flex;
    align-items: center;
    justify-content: center;
  }
  .business-card {
    position: relative;
    width: 1000px;
    height: 572px;
    background: radial-gradient(ellipse 70% 80% at 55% 45%, var(--navy-light) 0%, var(--navy-mid) 45%, var(--navy-deep) 100%);
    color: var(--white);
    overflow: hidden;
  }
  .brand {
    position: absolute;
    left: 560px;
    top: 70px;
    width: 380px;
    display: flex;
    flex-direction: column;
    align-items: center;
    gap: 22px;
  }
  .brand-mark {
    width: 90px;
    height: 90px;
    background: var(--silver);
  }
  .brand-name {
    font-size: 22px;
    font-weight: 400;
    letter-spacing: 4px;
    text-transform: uppercase;
    text-align: center;
    line-height: 1.35;
    color: var(--silver);
  }
  .address {
    position: absolute;
    left: 590px;
    top: 300px;
    font-size: 21px;
    line-height: 1.35;
  }
  .divider {
    position: absolute;
    left: 590px;
    top: 372px;
    width: 340px;
    height: 2px;
    background: var(--white);
  }
  .contact-list {
    position: absolute;
    left: 590px;
    top: 392px;
    list-style: none;
    font-size: 21px;
    line-height: 1.4;
  }
  .contact-label { font-weight: 700; margin-right: 6px; }
  .person {
    position: absolute;
    left: 70px;
    top: 370px;
  }
  .person-name {
    font-size: 40px;
    font-weight: 700;
    line-height: 1.1;
  }
  .person-title {
    font-size: 24px;
    font-weight: 400;
    margin-top: 4px;
    color: var(--silver);
  }
  .website {
    position: absolute;
    left: 110px;
    top: 488px;
    font-size: 22px;
  }
  .website strong { font-weight: 700; }
</style>
</head>
<body>
  <main class="canvas">
    <section class="business-card" aria-label="Business card for BriAnne Dockery">
      <div class="brand">
        <span class="brand-mark" aria-hidden="true"></span>
        <span class="brand-name">Harborlyte<br>Wealth Management</span>
      </div>

      <p class="address">20537 W. Marlowe PKWY Ste. B<br>Calderwick, QZ 00390</p>
      <div class="divider"></div>
      <ul class="contact-list">
        <li><span class="contact-label">Cell:</span>(555) 210-0173</li>
        <li><span class="contact-label">Direct:</span>(555) 310-0148</li>
        <li><span class="contact-label">Email:</span>brianne@harborwmx.com</li>
      </ul>

      <div class="person">
        <h1 class="person-name">BriAnne Dockery</h1>
        <p class="person-title">Executive Assistant</p>
      </div>
      <p class="website">www.<strong>harborwmx</strong>.com</p>
    </section>
  </main>
</body>
</html>
```